Talvora Web site

Talvora is a trade name for Brennick enterprises llc, would like Brennick mentioned but not prominent.

Use current logo to base colors and look/feel of website. Modern trendy look.

Talvora Technical Services - "Irrevocably committed to your success"

Website design for a nation wide service based company

Networking, AV, access control, automation, EAS, project management, consulting, electrical, design, service staffing

Hostwell hosts our URL's

Questions-
Who owns the content once accepted.
How is the content delivered to build site
How do we adjust. or add to content once published

Target Market(s)

commercial and retail technical services. IE, we provide technical services for retail and commercial vertical markets

Industry/Entity Type

Trade

Coding

Coded - Design and coding required

Number of Pages Required

5+ page

Font styles to use
Sans Serif

Colors
3276b5

Requirements
Must have
• Pages-
• About/info, contact, services, customers log in portal, social media links
• links to outside web based software portals
• Call through (call me) links

```html
<!DOCTYPE html>
<html lang="en">
<head>
<meta charset="utf-8">
<title>Talvora Technical Services</title>
<link href="https://fonts.googleapis.com/css2?family=Michroma&family=Roboto:wght@300;400;500;700&display=swap" rel="stylesheet">
<style>
:root{
  --blue:#3276b5;
  --blue-dark:#1f5a96;
  --green:#8cc63f;
  --page:#eeeef1;
  --white:#ffffff;
  --ink:#333;
  --muted:#8a8a8a;
  --line:#c9ccd2;
  --dark:#15171b;
}
*{box-sizing:border-box;margin:0;padding:0}
html,body{width:691px;height:1200px;overflow:hidden}
body{position:relative;background:var(--page);font-family:'Roboto',sans-serif;color:var(--ink)}
.abs{position:absolute}
.shapes{position:absolute;left:0;top:0}
.heading{font-family:'Michroma',sans-serif;font-size:9px;color:#222;letter-spacing:.2px;white-space:nowrap;line-height:1}
.heading-wrap{position:absolute;display:flex;align-items:center;gap:10px;padding-bottom:7px;border-bottom:1px solid var(--line);white-space:nowrap}
.heading-wrap svg{flex:none}
.heading-wrap::after{content:"";position:absolute;left:0;bottom:-1px;width:16px;height:2px;background:var(--blue)}
.heading-wrap.dark{border-color:#666}
.heading-wrap.dark .heading{color:#fff}

/* header */
.brand{left:92px;top:14px;display:flex;align-items:center;gap:6px}
.brand-mark{width:26px;height:26px;border-radius:50%;background:var(--blue)}
.brand-name{font-family:'Michroma',sans-serif;font-size:12px;color:var(--blue);line-height:1}
.brand-sub{font-size:5px;color:var(--blue);letter-spacing:.4px;margin-top:3px}
.phone{left:415px;top:13px;display:flex;align-items:center;gap:6px;font-size:10px;color:var(--blue);font-weight:500}
.account{left:513px;top:12px;display:flex;align-items:center;gap:6px;font-size:7.5px;color:#666}
.account .user{width:16px;height:16px;border:1px solid var(--line);display:flex;align-items:center;justify-content:center}
.nav{left:261px;top:51px;display:flex;font-size:7.5px;color:#555;font-weight:500;white-space:nowrap}
.nav a{color:inherit;text-decoration:none;padding-right:11px;margin-right:11px;position:relative}
.nav a::after{content:"\\";position:absolute;right:-3px;color:#bbb}
.nav a.active{color:var(--blue)}
.search{left:492px;top:49px;width:110px;font-size:7px;font-style:italic;color:#999;display:flex;justify-content:space-between}

/* hero */
.hero-caption{left:110px;top:305px;font-family:'Michroma',sans-serif;font-size:9.6px;color:var(--green);white-space:nowrap}
.btn-outline{border:1px solid #ccc;color:#eee;font-size:6.5px;display:flex;align-items:center;justify-content:center}
.hero-btn{left:509px;top:302px;width:70px;height:19px}
.hero-arrow{color:rgba(255,255,255,.5);font-size:30px;font-weight:300;top:150px}

/* welcome */
.welcome-text{left:263px;top:381px;width:339px;font-size:6.8px;line-height:12.1px;color:var(--muted);text-align:justify}
.read-more{left:548px;top:488px;width:54px;height:16px;border:1px solid var(--blue);color:var(--blue);font-size:5.8px;font-weight:500;display:flex;align-items:center;justify-content:center;background:#fff}

/* services */
.cards{left:88px;top:572px;display:flex;gap:12px}
.card{width:120px;height:155px;background:#fff;text-align:center;padding-top:13px}
.card.active{background:var(--blue)}
.card .icon{width:53px;height:53px;margin:0 auto;border-radius:50%;background:var(--blue);border:2px solid #cfe0f0;display:flex;align-items:center;justify-content:center}
.card.active .icon{background:#fff;border-color:#a9c6e4}
.card h3{font-family:'Michroma',sans-serif;font-weight:400;font-size:7.6px;color:var(--blue);margin:11px 0 8px;white-space:nowrap}
.card.active h3,.card.active p{color:#fff}
.card p{font-size:6px;line-height:10.2px;color:#888;padding:0 9px}
.svc-arrow{top:598px;font-size:34px;color:#777;font-weight:300}

/* testimonials */
.quote-box{left:111px;top:810px;width:367px;height:103px;background:rgba(0,0,0,.75);padding:26px 22px 0 24px}
.quote-box p{font-size:7px;line-height:14px;color:#6e7177;font-style:italic}
.quote-box .who{margin-top:12px;font-size:8.5px;color:#fff;font-weight:500}
.quote-box .who span{font-size:6px;font-weight:400}
.qmark{font-family:Georgia,serif;font-size:16px;color:#fff;font-weight:700}

/* contact */
.contact-item{display:flex;align-items:center;gap:10px;font-size:7px;line-height:12px;color:#666}
.contact-item .ico{width:33px;height:33px;border:1px solid var(--line);background:#fff;display:flex;align-items:center;justify-content:center}
.field{border:1px solid var(--line);background:#f4f4f6;font-size:7px;color:#999;padding:8px 9px}
.send{left:544px;top:1094px;width:58px;height:50px;background:var(--green);color:#fff;font-weight:700;font-size:11px;display:flex;align-items:center;justify-content:center}

/* footer */
.footer{left:0;top:1165px;width:691px;height:35px;background:#f7f7f8}
.copy{left:88px;top:1179px;font-size:6px;color:#777;white-space:nowrap}
.social{left:524px;top:1175px;display:flex;gap:5px}
.social span{width:16px;height:16px;border-radius:50%;border:1px solid #aaa}
.social span:first-child{background:var(--blue);border-color:var(--blue)}
</style>
</head>
<body>

<svg class="shapes" width="691" height="1200" viewBox="0 0 691 1200">
  <defs>
    <linearGradient id="heroGrad" x1="0" y1="0" x2="1" y2="1">
      <stop offset="0" stop-color="#c9d3dc"/>
      <stop offset=".5" stop-color="#e6e2dd"/>
      <stop offset="1" stop-color="#b9c3cc"/>
    </linearGradient>
    <linearGradient id="crowd" x1="0" y1="0" x2="0" y2="1">
      <stop offset="0" stop-color="#262a30"/>
      <stop offset="1" stop-color="#1a1c20"/>
    </linearGradient>
  </defs>
  <polygon points="0,60 691,60 691,264 625,327 66,327 0,264" fill="url(#heroGrad)" role="img" aria-label="Photo of three smiling office colleagues gathered around a laptop"/>
  <polygon points="88,296 625,296 602,327 66,327" fill="rgba(20,20,22,.85)"/>
  <polygon points="0,0 691,0 691,64 0,64" fill="var(--page)"/>
  <polygon points="44,0 625,0 600,64 88,64" fill="#fff"/>
  <polygon points="0,327 691,327 691,456 626,522 66,522 0,456" fill="#fff"/>
  <polygon points="0,681 691,681 691,890 624,955 64,955 0,890" fill="url(#crowd)" role="img" aria-label="Blurred photo of a large audience"/>
  <polygon points="604,681 691,681 604,745" fill="var(--page)"/>
  <circle cx="540" cy="863" r="38" fill="#fff"/>
  <circle cx="540" cy="863" r="34" fill="#d7c48f" role="img" aria-label="Portrait of a smiling client"/>
</svg>

<!-- header -->
<div class="abs brand">
  <div class="brand-mark"></div>
  <div>
    <div class="brand-name">TALVORA</div>
    <div class="brand-sub">TECHNICAL SERVICES</div>
  </div>
</div>
<div class="abs phone">
  <svg width="14" height="14" viewBox="0 0 14 14"><circle cx="7" cy="7" r="7" fill="var(--green)"/><path d="M4.5 4c.5 2.5 2.5 4.7 5 5.5l.8-1.2-1.6-.9-.7.7c-1-.5-1.8-1.3-2.3-2.3l.7-.7-.9-1.6z" fill="#fff"/></svg>
  555.014.2290
</div>
<div class="abs account">
  <span class="user"><svg width="9" height="9" viewBox="0 0 9 9"><circle cx="4.5" cy="2.8" r="2" fill="var(--blue)"/><path d="M1 9c0-2.2 1.6-3.6 3.5-3.6S8 6.8 8 9z" fill="var(--blue)"/></svg></span>
  Login <span style="color:#bbb">\</span> Register
</div>
<nav class="abs nav">
  <a class="active">HOME</a><a>ABOUT US</a><a>SERVICES</a><a>CONTACT US</a>
</nav>
<div class="abs search">Search
  <svg width="10" height="10" viewBox="0 0 10 10"><circle cx="6" cy="4" r="3.2" fill="none" stroke="var(--blue)" stroke-width="1.2"/><path d="M3.7 6.3L1 9" stroke="var(--blue)" stroke-width="1.3"/></svg>
</div>

<!-- hero -->
<div class="abs hero-arrow" style="left:64px">&#8249;</div>
<div class="abs hero-arrow" style="left:610px">&#8250;</div>
<div class="abs hero-caption">IRREVOCABLY COMMITTED TO YOUR SUCCESS</div>
<div class="abs btn-outline hero-btn">LEARN MORE</div>

<!-- welcome -->
<div class="abs" style="left:88px;top:338px;width:197px;height:162px;background:linear-gradient(90deg,#cfd2d6,#eef0f2 70%,#fff)" role="img" aria-label="Photo of a businesswoman with a coffee cup at her laptop"></div>
<div class="heading-wrap" style="left:262px;top:344px;width:125px">
  <svg width="12" height="12" viewBox="0 0 13 13"><circle cx="6.5" cy="3.5" r="3" fill="var(--blue)"/><path d="M0 13c0-3.8 2.8-6 6.5-6S13 9.2 13 13z" fill="var(--blue)"/></svg>
  <span class="heading">WELCOME TALVORA</span>
</div>
<p class="abs welcome-text">Lorem ipsum dolor sit amet, consectetur adipiscing elit. Morbi id ex sit amet lorem bibendum sodales. Aenean diam justo, vulputate quis dui vitae, rutrum maximus ipsum. Cum sociis natoque penatibus et magnis dis parturient montes, nascetur ridiculus mus. Lorem ipsum dolor sit amet, consectetur adipiscing elit. Vestibulum ante ipsum primis in faucibus orci luctus et ultrices posuere cubilia Curae; Aliquam sit amet volutpat erat, vel tincidunt diam. Sed tincidunt mi eu felis pretium, vel aliquam est ultrices. Etiam hendrerit leo dignissim, fringilla sem sed, egestas augue. Quisque ullamcorper sem lorem, id maximus dolor interdum vitae. Fusce suscipit quam sit amet sapien molestie sodales. Donec quis suscipit lorem. Donec aliquam tristique sem. Etiam egestas nulla a est accumsan, ut venenatis lorem porttitor.</p>
<div class="abs read-more">READ MORE</div>

<!-- services -->
<div class="heading-wrap" style="left:88px;top:541px;width:130px">
  <svg width="13" height="13" viewBox="0 0 14 14"><circle cx="7" cy="7" r="5" fill="none" stroke="var(--blue)" stroke-width="3" stroke-dasharray="2.2 1.7"/><circle cx="7" cy="7" r="3.6" fill="var(--blue)"/><circle cx="7" cy="7" r="1.6" fill="var(--page)"/></svg>
  <span class="heading">OUR SERVICES</span>
</div>
<div class="abs svc-arrow" style="left:64px">&#8249;</div>
<div class="abs svc-arrow" style="left:612px">&#8250;</div>
<div class="abs cards">
  <div class="card active">
    <div class="icon"><svg width="30" height="24" viewBox="0 0 30 24"><g fill="var(--blue)"><circle cx="15" cy="6" r="4"/><circle cx="6" cy="9" r="3"/><circle cx="24" cy="9" r="3"/><path d="M8 22c0-5 3-8 7-8s7 3 7 8z"/><path d="M0 22c0-4 2.5-6 6-6 1.5 0 2.5.4 3 1-1 1.5-1.5 3-1.5 5z"/><path d="M30 22c0-4-2.5-6-6-6-1.5 0-2.5.4-3 1 1 1.5 1.5 3 1.5 5z"/></g></svg></div>
    <h3>NETWORKING</h3>
    <p>Lorem ipsum dolor sit amet nsect etur adipiscing elit. Mrbi id ex sit amet lorem bibeas ndum sodales. Aenean diam jus ntibus et magnis dis parturient....</p>
  </div>
  <div class="card">
    <div class="icon"><svg width="24" height="24" viewBox="0 0 24 24" fill="none" stroke="#fff" stroke-width="1.6"><rect x="3" y="2" width="15" height="18"/><rect x="6" y="5" width="9" height="4"/><path d="M6 12h2M10 12h2M14 12h1M6 15h2M10 15h2"/><path d="M14 16l6 6" stroke-width="2"/></svg></div>
    <h3>ACCESS CONTROL</h3>
    <p>Lorem ipsum dolor sit amet nsect etur adipiscing elit. Mrbi id ex sit amet lorem bibeas ndum sodales. Aenean diam jus ntibus et magnis dis parturient....</p>
  </div>
  <div class="card">
    <div class="icon"><svg width="26" height="26" viewBox="0 0 26 26" fill="none" stroke="#fff"><path d="M4 13a9 9 0 0 1 15-6.7M22 13a9 9 0 0 1-15 6.7" stroke-width="2"/><path d="M19 2v5h-5M7 24v-5h5" stroke-width="2"/><circle cx="13" cy="13" r="4" stroke-width="3" stroke-dasharray="2 1.5"/></svg></div>
    <h3>AUTOMATION</h3>
    <p>Lorem ipsum dolor sit amet nsect etur adipiscing elit. Mrbi id ex sit amet lorem bibeas ndum sodales. Aenean diam jus ntibus et magnis dis parturient....</p>
  </div>
  <div class="card">
    <div class="icon"><svg width="26" height="24" viewBox="0 0 26 24" fill="none" stroke="#fff" stroke-width="1.8"><rect x="2" y="2" width="22" height="15"/><path d="M9 22h8M13 17v5"/><path d="M8 14l9-9" stroke-width="2.2"/></svg></div>
    <h3>DESIGN</h3>
    <p>Lorem ipsum dolor sit amet nsect etur adipiscing elit. Mrbi id ex sit amet lorem bibeas ndum sodales. Aenean diam jus ntibus et magnis dis parturient....</p>
  </div>
</div>

<!-- testimonials -->
<div class="heading-wrap dark" style="left:112px;top:765px;width:178px">
  <svg width="12" height="12" viewBox="0 0 13 13"><circle cx="6.5" cy="3.5" r="3" fill="var(--blue)"/><path d="M0 13c0-3.8 2.8-6 6.5-6S13 9.2 13 13z" fill="var(--blue)"/></svg>
  <span class="heading">CLIENT TESTIMONALS</span>
</div>
<div class="abs quote-box">
  <span class="abs qmark" style="left:9px;top:4px">&ldquo;</span>
  <p>Lorem ipsum dolor sit amet, consectetur adipiscing elit. Morbi id ex sit amet lorem bindum sodales. Aenean diam justo, vulputate quis dui vitae, rutrum maximus ipsum. Cum sociis natoque penatibus et magnis dis parturient montes, nascetur ridiculus mus.</p>
  <span class="abs qmark" style="right:9px;top:56px">&rdquo;</span>
  <div class="who">Lorem ispum <span>- Compny Name</span></div>
</div>

<!-- contact -->
<div class="heading-wrap" style="left:88px;top:971px;width:129px">
  <svg width="13" height="15" viewBox="0 0 14 16" fill="none" stroke="var(--blue)" stroke-width="1.4"><rect x="1" y="1" width="8" height="13" rx="1"/><path d="M7 9l5 5M9 7c2 0 3.5 1.5 3.5 3.5"/></svg>
  <span class="heading">GET IN TOUCH</span>
</div>
<div class="abs contact-item" style="left:88px;top:1005px">
  <span class="ico"><svg width="14" height="16" viewBox="0 0 14 16" fill="none" stroke="var(--blue)" stroke-width="1.6"><path d="M7 15S1.5 9.5 1.5 6a5.5 5.5 0 0 1 11 0C12.5 9.5 7 15 7 15z"/><circle cx="7" cy="6" r="2"/></svg></span>
  <span>Lorem ipsum dolor sit am<br>consectetur adipiscing 25252525</span>
</div>
<div class="abs contact-item" style="left:307px;top:1005px">
  <span class="ico"><svg width="14" height="14" viewBox="0 0 14 14" fill="var(--blue)"><path d="M2 2c.6 4.5 4.6 9 10 10l1-2.4-2.6-1.4-1.2 1.2C7.4 8.6 5.6 6.8 4.8 5L6 3.8 4.4 1z"/></svg></span>
  <span>555 014 2290<br>555 014 7731</span>
</div>
<div class="abs contact-item" style="left:470px;top:1005px">
  <span class="ico"><svg width="16" height="13" viewBox="0 0 16 13" fill="none" stroke="var(--blue)" stroke-width="1.5"><rect x="1" y="3" width="14" height="9"/><path d="M1 3l7 5 7-5"/></svg></span>
  <span>info@talvoratech.com</span>
</div>

<div class="abs field" style="left:88px;top:1061px;width:163px;height:22px">Your Name</div>
<div class="abs field" style="left:264px;top:1061px;width:163px;height:22px">Your E-mail</div>
<div class="abs field" style="left:440px;top:1061px;width:162px;height:22px">Your Phone</div>
<div class="abs field" style="left:88px;top:1094px;width:443px;height:50px">Your Message</div>
<div class="abs send">SEND</div>

<!-- footer -->
<div class="abs footer"></div>
<div class="abs copy">Copyright © 2015 Talvora, a Brennick enterprises llc company. All rights reserved.</div>
<div class="abs social" aria-label="Social media links"><span></span><span></span><span></span><span></span></div>

</body>
</html>
```